FUN WEBSITE NEEDED FOR NEW ACCESSORY PRINTING COMPANY

NOTE: This is Website Design Only - No coding required

PLEASE SUBMIT YOUR DESIGNS RIGHT AWAY AS WE WANT TO PICK A WINNER ASAP!

Hi,

We are looking for a vibrant and hip website for a new emerging industry that allows us to personalize cell phone covers and many other items with our unique printing ability.

Our site must be hip and vibrant, as our audience is high schoolers and teens for the most part.

The site should be simple and straight forward while at the same time be of high visual quality.

This will be an e-commerce site that will sell around 10 products.

Please provide designs for a great looking site to help us sell our products.

You will find our logo attached. Here is a link to our catalogue so you can get an idea of what we do. Again Cell Phone Covers will be our main priority so please focus on that.

https://www.filevault-example.net/s/qetumaxlor7261/SnapGlo%20Catalog%2011x17.pdf

Thanks!
Todd

Target Market(s)

The target market is high schoolers and teens.

Additional target market is Collage kids

Sports Teams

Industry/Entity Type

Cell Phone

Font styles to use
Sans Serif

Requirements
Must have
• Clean look
Ecommerce
Horizontal menu
Showing cell phone printing from catalogue
Follow Logo Colors
Should not have
• Cluttery design
Hard to read see
Not clean

```html
<!DOCTYPE html>
<html lang="en">
<head>
<meta charset="utf-8">
<title>SnapGlo – Unlimited Personalized Products</title>
<link href="https://fonts.googleapis.com/css2?family=Comic+Neue:wght@400;700&family=Arimo:wght@400;700&display=swap" rel="stylesheet">
<style>
:root{
  --green:#3ca74a;
  --green-dark:#2f9a3e;
  --green-deep:#23873a;
  --page:#f2f0f1;
  --blue:#4a1de6;
  --text:#2b2b2b;
  --link:#2a9a3c;
  --red:#d0453f;
  --yellow:#f5e21c;
  --white:#ffffff;
}
*{box-sizing:border-box;margin:0;padding:0}
html,body{width:1200px;height:1036px;overflow:hidden}
body{position:relative;background:var(--page);font-family:"Comic Neue",cursive;color:var(--text)}
a{color:inherit}
.abs{position:absolute}
.topbar{left:0;top:0;width:1200px;height:33px;background:var(--green);border-bottom:1px solid #6cc576;color:var(--white);font-weight:700;font-size:13px}
.topbar .left{left:216px;top:9px}
.topbar .right{right:199px;top:9px}
.navbar{left:0;top:34px;width:1200px;height:42px;background:linear-gradient(#3aa649,#2e9b3f);box-shadow:0 4px 4px #b9b9b9;color:var(--white);font-family:"Arimo",sans-serif;font-size:12px;font-weight:700}
.phone{left:218px;top:15px;display:flex;gap:8px;align-items:center}
.menu{left:445px;top:9px;display:flex}
.menu span{display:block;width:76px;height:24px;line-height:22px;text-align:center;margin-right:6px}
.menu .active{background:var(--green-dark);border:1px solid #58bd66;border-radius:3px}
.search{left:788px;top:11px;width:108px;height:22px;background:var(--green-deep);border-radius:4px;font-style:italic;font-weight:400;font-size:10px;padding:5px 9px}
.cart{left:925px;top:15px;display:flex;gap:6px;align-items:center}
.slider{left:187px;top:76px;width:825px;height:313px;background:linear-gradient(120deg,#c9b2a0 0%,#d7c8a2 30%,#aeb9a4 50%,#7d8b88 65%,#c6d0cf 100%);overflow:hidden}
.brand{left:100px;top:98px;width:200px;text-align:center;font-size:40px;font-weight:700;color:var(--white)}
.headline{left:406px;top:100px;font-size:29px;font-weight:700;line-height:37px;width:400px;white-space:nowrap}
.headline .y{color:var(--yellow)}.headline .r{color:var(--red)}.headline .b{color:var(--blue)}
.cta{left:405px;top:194px;width:153px;height:58px;background:var(--red);border:2px solid #a82a28;border-radius:4px;color:var(--yellow);font-weight:700;font-size:19px;line-height:21px;text-align:center;padding-top:7px}
.arrow{top:202px;width:56px;height:44px;background:#3b3b3b;opacity:.85}
.dots{left:386px;top:287px;display:flex;gap:9px}
.dots i{width:12px;height:12px;border-radius:50%;background:#222}
.dots i.on{background:none;border:2px solid #222}
.divider{left:900px;top:389px;width:2px;height:424px;background:#fff}
h2{position:absolute;font-size:18px;font-weight:700;color:var(--blue)}
.services{left:241px;top:443px;list-style:none;font-family:"Arimo",sans-serif;font-size:11px}
.services li{height:21.2px;display:flex;align-items:center;gap:9px}
.more{display:flex;align-items:center;gap:8px;font-weight:700;font-size:12.5px;color:var(--link);text-decoration:underline}
.more b{display:inline-block;width:20px;height:16px;background:var(--green);border-radius:3px;position:relative}
.more b::after{content:"";position:absolute;left:6px;top:6px;border:4px solid transparent;border-top:5px solid #fff}
.body-text{font-family:"Arimo",sans-serif;font-size:9.5px;line-height:12px;color:#333}
.date{font-weight:700;font-size:12.5px;color:#333}
.ph{border:1px solid #8fbf95}
.offer{left:731px;top:661px;width:236px;height:72px;background:linear-gradient(#3fb04e,#2c9a3c);border:2px solid #23873a;border-radius:5px;color:#fff;font-family:"Arimo",sans-serif;padding:10px 22px}
.offer .t{font-size:16px;font-weight:700}
.offer .s{font-size:9px}
.offer .r{font-size:11px;text-decoration:underline;margin-top:10px}
.footer{left:0;top:813px;width:1200px;height:180px;background:linear-gradient(#3ca74a,#2f9a3f);color:#fff;font-weight:700}
.footer h3{position:absolute;font-size:14.5px}
.footer .txt{position:absolute;font-size:11.5px}
.social{left:731px;top:53px;display:flex;gap:13px}
.social i{width:18px;height:18px;border-radius:4px;background:#fff;display:block}
.email{left:731px;top:104px;width:142px;height:22px;background:var(--green-deep);border:1px solid #52b361;border-radius:3px;font-style:italic;font-size:10px;padding:5px 6px}
.legal{left:0;top:993px;width:1200px;height:43px;background:var(--green-dark);border-top:1px solid #5cbc6a;color:#fff;font-weight:700;font-size:14px}
.cards{left:208px;top:11px;display:flex;gap:8px}
.cards i{display:block;width:33px;height:18px;border-radius:2px;background:#e6efe6}
.cards i:nth-child(1){background:#2a5aa8}.cards i:nth-child(4){background:#2b5fb3}.cards i:nth-child(5){background:#3a3a3a}
</style>
</head>
<body>
<header>
  <div class="abs topbar">
    <div class="abs left">Order Status &nbsp;|&nbsp; Wish List</div>
    <div class="abs right">LogIn &nbsp;&nbsp;|&nbsp;&nbsp; Register &nbsp;&nbsp;|&nbsp;&nbsp; My Account</div>
  </div>
  <nav class="abs navbar">
    <div class="abs phone"><svg width="11" height="11" viewBox="0 0 24 24"><path fill="#fff" d="M6.6 10.8a15 15 0 0 0 6.6 6.6l2.2-2.2c.3-.3.7-.4 1-.2 1.1.4 2.3.6 3.6.6.6 0 1 .4 1 1V20c0 .6-.4 1-1 1A17 17 0 0 1 3 4c0-.6.4-1 1-1h3.5c.6 0 1 .4 1 1 0 1.3.2 2.5.6 3.6.1.3 0 .7-.2 1z"/></svg>123 - 456 -7890</div>
    <div class="abs menu"><span class="active">Home</span><span>Products</span><span>Specials</span><span>Galleries</span></div>
    <div class="abs search">Search...
      <svg class="abs" style="right:8px;top:6px" width="10" height="10" viewBox="0 0 10 10"><circle cx="4" cy="4" r="3" stroke="#fff" stroke-width="1.5" fill="none"/><path d="M6.3 6.3 9 9" stroke="#fff" stroke-width="1.5"/></svg></div>
    <div class="abs cart"><svg width="12" height="11" viewBox="0 0 12 11"><path d="M0 1h2l2 6h6l1.5-4.5H3" stroke="#fff" stroke-width="1.4" fill="none"/><circle cx="5" cy="9.5" r="1" fill="#fff"/><circle cx="9" cy="9.5" r="1" fill="#fff"/></svg>Cart : $0.00</div>
  </nav>
</header>

<section class="abs slider" role="img" aria-label="Photo of a loupe magnifier over colour printing proof charts">
  <div class="abs brand">SnapGlo</div>
  <div class="abs headline"><span class="y">UNLIMITED</span> <span class="r">PERSONALIZED</span><br><span class="b">PRODUCTS</span></div>
  <div class="abs cta">To Our<br>Catalogue</div>
  <div class="abs dots"><i></i><i class="on"></i><i></i></div>
</section>
<div class="abs arrow" style="left:180px"><svg width="56" height="44"><path d="M32 12 22 22l10 10" stroke="#888" stroke-width="4" fill="none"/></svg></div>
<div class="abs arrow" style="left:964px"><svg width="56" height="44"><path d="M24 12l10 10-10 10" stroke="#888" stroke-width="4" fill="none"/></svg></div>

<div class="abs divider"></div>

<main>
  <h2 style="left:241px;top:420px">Featured Services</h2>
  <ul class="abs services">
    <li><span style="color:#f2b632">★</span>Phone Covers</li>
    <li><span style="color:#f2b632">★</span>Pet Items</li>
    <li><span style="color:#f2b632">★</span>Sublislate and Photo Frames</li>
    <li><span style="color:#f2b632">★</span>Holiday Gifts</li>
    <li><span style="color:#f2b632">★</span>Children and Baby Gifts</li>
    <li><span style="color:#f2b632">★</span>Awards and Emblems</li>
    <li><span style="color:#f2b632">★</span>Eyeglass Accessories</li>
    <li><span style="color:#f2b632">★</span>Wearables</li>
  </ul>
  <a class="abs more" style="left:241px;top:623px"><b></b>All Services</a>

  <div class="abs" style="left:486px;top:420px;font-family:Arimo,sans-serif;font-size:26px;color:#555">Get Free</div>
  <div class="abs" style="left:488px;top:448px;font-family:Arimo,sans-serif;font-size:10px;color:var(--red)">BUSINESS CARDS</div>
  <div class="abs" role="img" aria-label="Illustration of red and green wrapped gift boxes" style="left:604px;top:427px;width:86px;height:55px;background:linear-gradient(90deg,#8fcf5a,#e24a4a);border-radius:4px"></div>
  <a class="abs more" style="left:486px;top:475px"><b></b>More Details</a>

  <h2 style="left:487px;top:524px">Cell Phone Covers</h2>
  <div class="abs ph" role="img" aria-label="Banner of personalized printed cell phone covers – professional print cover" style="left:487px;top:553px;width:194px;height:74px;background:linear-gradient(#3ec65a,#6be07a)"></div>
  <p class="abs body-text" style="left:487px;top:642px;width:195px">Lorem Ipsum is simply dummy text of the printing and typesetting industry.Lorem Ipsum has been the industry's standard dummy text ever since the 1500s,</p>
  <a class="abs more" style="left:486px;top:701px"><b></b>More Products</a>

  <h2 style="left:731px;top:420px">News &amp; Events</h2>
  <div class="abs date" style="left:731px;top:459px">May 26, 2014</div>
  <p class="abs body-text" style="left:731px;top:477px;width:192px">Lorem Ipsum is simply dummy text of the printing and typesetting industry.Lorem Ipsum has been the industry's standard dummy text ever since the 1500s,</p>
  <a class="abs more" style="left:854px;top:514px;font-size:11px">More Details</a>
  <div class="abs date" style="left:731px;top:543px">May 20, 2014</div>
  <p class="abs body-text" style="left:731px;top:561px;width:192px">Lorem Ipsum is simply dummy text of the printing and typesetting industry.Lorem Ipsum has been the industry's standard dummy text ever since the 1500s,</p>
  <a class="abs more" style="left:854px;top:598px;font-size:11px">More Details</a>
  <a class="abs more" style="left:731px;top:617px"><b></b>All News</a>

  <div class="abs offer"><div class="t">Special Offer</div><div class="s">Lorem Ipsum dolor sit amet</div><div class="r">› Read More</div></div>
  <div class="abs" role="img" aria-label="Illustration of a paint can with colour swatch fan" style="left:880px;top:652px;width:110px;height:106px;background:linear-gradient(135deg,#e8e8e8,#f0c23a 40%,#e04444 65%,#2a5fd0);border-radius:8px"></div>
</main>

<footer class="abs footer">
  <h3 style="left:241px;top:27px">Business Identity</h3>
  <div class="txt" style="left:248px;top:60px;line-height:22px">
    <div><span style="color:#d04fd0">●</span>&nbsp;&nbsp; Aenean nonummy hendrerit.</div>
    <div><span style="color:#1a22d8">●</span>&nbsp;&nbsp; Maurisha sellus porta fusce.</div>
    <div><span style="color:#e8e23a">●</span>&nbsp;&nbsp; Suscipit varius natoque penatibu.</div>
  </div>
  <a class="txt" style="left:241px;top:138px;text-decoration:underline">Read more</a>
  <h3 style="left:485px;top:27px">Contact Information</h3>
  <div class="txt" style="left:486px;top:66px;line-height:13px">
    <svg width="11" height="11" viewBox="0 0 24 24" style="vertical-align:-1px"><path fill="#fff" d="M6.6 10.8a15 15 0 0 0 6.6 6.6l2.2-2.2c.3-.3.7-.4 1-.2 1.1.4 2.3.6 3.6.6.6 0 1 .4 1 1V20c0 .6-.4 1-1 1A17 17 0 0 1 3 4c0-.6.4-1 1-1h3.5c.6 0 1 .4 1 1 0 1.3.2 2.5.6 3.6.1.3 0 .7-.2 1z"/></svg>
    &nbsp;123 - 456 -7890<br>&nbsp;&nbsp;&nbsp;&nbsp;&nbsp;&nbsp;123 - 456 -7890
  </div>
  <div class="txt" style="left:486px;top:101px"><svg width="12" height="9" viewBox="0 0 12 9" style="vertical-align:0"><rect width="12" height="9" fill="#fff"/><path d="M0 0l6 5 6-5" stroke="#2f9a3f" fill="none"/></svg>&nbsp; contact@snapglo.example</div>
  <h3 style="left:731px;top:27px">Follow Us</h3>
  <div class="abs social"><i></i><i></i><i></i><i></i><i></i></div>
  <h3 style="left:731px;top:83px">Subscribe</h3>
  <div class="abs email">Your email...</div>
  <a class="txt" style="left:822px;top:138px;text-decoration:underline">Subscribe</a>
</footer>

<div class="abs legal">
  <div class="abs cards"><i></i><i></i><i></i><i></i><i></i><i></i></div>
  <div class="abs" style="left:757px;top:12px">© Copyright 2014. All Rights Reserved</div>
</div>
</body>
</html>
```